Morrow Poolworks, LLC Business Card

We have a well designed logo that we need incorporated into a professional and unique business card. Morrow Poolworks provides professional swimming pool management. From openings to closings, inspections, chemicals, maintenance, lifeguard, safety audits, learn to swim lessons, etc. etc.
Different colors of blue are ideal. The final design should include water, clean water (very clean crystal clear water), and perhaps safety.
content/design ideas:
Felix Brant, President - Owner
felix@morrowpoolworks.example
office: 555-410-3826
cell: 555-962-1507
www.morrowpoolworks.example
"Your Pool: Safer, Cleaner, Clearer"
Target Market(s)
Our customers are mostly home owners associations and property management companies. Adults, aged 25 to 55. Mostly with young children.
Industry/Entity Type
Safety
Look and feel

```html
<!DOCTYPE html>
<html lang="en">
<head>
<meta charset="utf-8">
<title>Morrow Poolworks, LLC Business Card</title>
<link rel="stylesheet" href="https://fonts.googleapis.com/css2?family=Arimo:wght@400;700&display=swap">
<style>
  :root {
    --backdrop: #262626;
    --card-white: #f4f5f6;
    --pool-deep: #1e8fd6;
    --pool-mid: #3fb1ec;
    --pool-light: #7fd3f6;
    --brand-blue: #2f86c8;
    --ink: #2b2b2b;
    --ink-soft: #4a4a4a;
    --label-blue: #3f7fc0;
    --rule: #8a9bb0;
  }
  * { margin: 0; padding: 0; box-sizing: border-box; }
  html, body {
    width: 1200px; height: 896px; overflow: hidden;
    background: var(--backdrop);
    font-family: "Arimo", Arial, sans-serif;
  }
  .stage { position: relative; width: 1200px; height: 896px; }

  .card-front {
    position: absolute; left: 208px; top: 325px;
    width: 485px; height: 270px; overflow: hidden;
  }
  .pool-photo {
    position: absolute; inset: 0;
    background:
      radial-gradient(ellipse at 70% 55%, var(--pool-light) 0%, transparent 55%),
      linear-gradient(135deg, var(--pool-mid) 0%, var(--pool-deep) 100%);
  }
  .tagline {
    position: absolute; left: 26px; top: 26px;
    color: #ffffff; font-size: 19px; line-height: 24px; font-weight: 400;
  }

  .card-back {
    position: absolute; left: 757px; top: 218px;
    width: 277px; height: 485px;
    background: var(--card-white);
  }
  .brand {
    position: absolute; left: 30px; top: 108px;
    display: flex; align-items: center; gap: 10px;
  }
  .brand-dot {
    width: 14px; height: 14px; border-radius: 50%;
    background: var(--brand-blue); flex: none;
  }
  .brand-name {
    color: var(--brand-blue); font-weight: 700;
    font-size: 27px; line-height: 30px;
  }
  .person { position: absolute; left: 68px; top: 253px; }
  .person-name { font-size: 18px; color: var(--ink); letter-spacing: 0.3px; }
  .person-role { font-size: 13px; color: var(--ink-soft); margin-top: 3px; }

  .contacts {
    position: absolute; left: 68px; top: 323px;
    list-style: none; font-size: 12.5px; color: var(--ink); line-height: 16px;
  }
  .contacts li { display: flex; }
  .contacts .label { color: var(--label-blue); width: 24px; }
  .rule {
    position: absolute; left: 68px; top: 392px;
    width: 186px; height: 1px; background: var(--rule);
  }
  .website {
    position: absolute; left: 68px; top: 402px;
    font-size: 13px; color: var(--label-blue); letter-spacing: 0.6px;
  }
</style>
</head>
<body>
<main class="stage">
  <section class="card-front">
    <div class="pool-photo" role="img" aria-label="Photo of a woman in a sun hat relaxing on a blue inner tube in clear pool water"></div>
    <p class="tagline">YOUR POOL:<br>Safer, Cleaner, Clearer</p>
  </section>

  <section class="card-back">
    <div class="brand">
      <span class="brand-dot"></span>
      <span class="brand-name">Morrow<br>Poolworks</span>
    </div>
    <div class="person">
      <p class="person-name">FELIX BRANT</p>
      <p class="person-role">President - Owner</p>
    </div>
    <ul class="contacts">
      <li><span class="label">T</span>555-410-3826</li>
      <li><span class="label">M</span>555-962-1507</li>
      <li><span class="label">E</span>felix@morrowpoolworks.example</li>
    </ul>
    <div class="rule"></div>
    <p class="website">www.morrowpoolworks.example</p>
  </section>
</main>
</body>
</html>
```